Billboard design 8x3M NURA (Spanish company)

We´re located in the south of Spain. We run a local telecom company.
We sell Fiber optic, and mobile phone lines mainly.
The billboard will have to be in Spanish, I would like the price to be something you spot on first sight when passing by in the car.
Our company color is blue, like in our logo which I will add. I will also add a example from what we currently have.
The new offer should be:
1000 megas + 100Gigas movil con llamadas ilimitadas. (meaning 1000Mb fiber optic speed and 100Gb data and unlimited calls for 1 mobile line)
Our details are: phone line 952 00 0147
Website: nu-ra.es

```html
<!DOCTYPE html>
<html lang="es">
<head>
<meta charset="utf-8">
<title>NURA – Valla 1000 Megas + 100 Gigas</title>
<link rel="stylesheet" href="https://fonts.googleapis.com/css2?family=Lexend:wght@300;400;500;700&family=Oswald:wght@600&display=swap">
<style>
  :root {
    --page: #ffffff;
    --blue-deep: #0d3a62;
    --blue-mid: #17679a;
    --blue-light: #1f78a8;
    --night: #0a1f6a;
    --glow: #3fb6ff;
    --gold: #e3ae12;
    --white: #ffffff;
    --box: rgba(16, 52, 78, 0.85);
  }
  * { margin: 0; padding: 0; box-sizing: border-box; }
  html, body { width: 1200px; height: 588px; overflow: hidden; background: var(--page); }
  .canvas { position: relative; width: 1200px; height: 588px; }

  .billboard {
    position: absolute; left: 112px; top: 106px; width: 983px; height: 368px;
    overflow: hidden;
    background: linear-gradient(120deg, var(--blue-mid) 0%, var(--blue-light) 40%, var(--blue-deep) 100%);
    font-family: "Lexend", sans-serif; color: var(--white);
  }
  .backdrop { position: absolute; inset: 0; }

  .tag {
    position: absolute; left: 45px; top: 45px; height: 28px; padding: 0 6px;
    background: var(--gold); border-radius: 5px;
    font-size: 25px; font-weight: 500; line-height: 28px;
  }
  .headline { position: absolute; left: 45px; top: 86px; font-weight: 700; font-size: 55px; line-height: 55px; letter-spacing: -1.5px; }
  .headline .plus { color: var(--gold); }
  .subline { position: absolute; left: 50px; top: 198px; font-size: 26px; font-weight: 400; letter-spacing: 0.4px; }
  .price {
    position: absolute; left: 52px; top: 228px; color: var(--gold);
    font-family: "Oswald", sans-serif; font-weight: 600; font-size: 118px; line-height: 118px; letter-spacing: -4px;
  }

  .hand-photo { position: absolute; left: 497px; top: 34px; width: 198px; height: 334px; }

  .brand { position: absolute; left: 741px; top: 26px; width: 190px; text-align: center; }
  .brand-name { font-weight: 700; font-size: 60px; line-height: 56px; letter-spacing: 2px; }
  .brand-services { margin-top: 6px; font-weight: 500; font-size: 19px; white-space: nowrap; }

  .contact {
    position: absolute; left: 640px; top: 280px; width: 299px; height: 73px;
    background: var(--box); border: 2px solid var(--gold); border-radius: 10px;
  }
  .contact-phone {
    position: absolute; left: 10px; top: 6px; display: flex; align-items: center; gap: 5px;
    font-weight: 700; font-size: 35px; line-height: 38px; letter-spacing: -0.5px; white-space: nowrap;
  }
  .contact-web { position: absolute; right: 14px; top: 42px; font-weight: 300; font-size: 23px; letter-spacing: 0.8px; }
</style>
</head>
<body>
<div class="canvas">
  <section class="billboard">
    <svg class="backdrop" width="983" height="368" viewBox="0 0 983 368" aria-hidden="false">
      <defs>
        <linearGradient id="leftShade" x1="0" y1="0" x2="1" y2="1">
          <stop offset="0" stop-color="#17679a"/>
          <stop offset="0.5" stop-color="#1d6f9f"/>
          <stop offset="1" stop-color="#0d3a62"/>
        </linearGradient>
        <radialGradient id="lightTrails" cx="0.75" cy="0.5" r="0.75">
          <stop offset="0" stop-color="#bfe9ff"/>
          <stop offset="0.2" stop-color="#3fb6ff"/>
          <stop offset="0.55" stop-color="#1b5fcf"/>
          <stop offset="1" stop-color="#0a1f6a"/>
        </radialGradient>
      </defs>
      <rect width="983" height="368" fill="url(#leftShade)"/>
      <path d="M 70 0 L 330 260" stroke="#0f4c78" stroke-width="1" opacity="0.6"/>
      <path d="M 0 60 L 150 200" stroke="#0f4c78" stroke-width="1" opacity="0.6"/>
      <g role="img" aria-label="Estelas de luz azul de fibra óptica sobre fondo nocturno">
        <path d="M 516 0 C 545 60, 570 130, 590 200 L 620 368 L 983 368 L 983 0 Z" fill="url(#lightTrails)"/>
      </g>
      <path d="M 515 0 C 525 15, 532 30, 540 45" stroke="#e3ae12" stroke-width="5" fill="none"/>
    </svg>

    <div class="tag">Disfrutar</div>
    <h1 class="headline">1000 Megas <span class="plus">+</span><br>100 Gigas movil</h1>
    <p class="subline">con llamadas ilimitadas.</p>
    <p class="price">35€</p>

    <svg class="hand-photo" viewBox="0 0 198 334" role="img" aria-label="Mano sosteniendo un móvil con un test de velocidad">
      <defs>
        <linearGradient id="handTone" x1="0" y1="0" x2="1" y2="1">
          <stop offset="0" stop-color="#1a2f8f"/>
          <stop offset="1" stop-color="#0c1a5a"/>
        </linearGradient>
      </defs>
      <path d="M 10 20 Q 10 4 28 2 L 110 0 Q 126 0 130 14 L 195 270 Q 198 290 180 294 L 95 320 Q 80 322 76 308 Z" fill="url(#handTone)"/>
    </svg>

    <div class="brand">
      <div class="brand-name">NURA</div>
      <div class="brand-services">Wifi I Fibra I Movil I Tv</div>
    </div>

    <div class="contact">
      <div class="contact-phone">
        <svg width="16" height="28" viewBox="0 0 16 28" aria-hidden="true">
          <rect x="1.5" y="1.5" width="13" height="25" rx="2.5" fill="none" stroke="#fff" stroke-width="2"/>
          <circle cx="8" cy="22.5" r="1.3" fill="#fff"/>
        </svg>
        <span>952 00 0147</span>
      </div>
      <div class="contact-web">www.nu-ra.es</div>
    </div>
  </section>
</div>
</body>
</html>
```